Create Bourbon label for Craft Distillery located in the Foothills of NC.

Need to create a label for a craft bourbon. The brand name is Creekhollow. Looking for a traditional/vintage bottle label. I have created a concept and would like an expansion of the concept idea (open to artwork outside of concept art as well). I have included the bottle being used. Label area approx 4.25H x 3.5W. With the Creekhollow brand name, would like to incorporate trees (native to NC and Appalachia), mountains (mt pano of area included), and sawblade. However, I do not want the sawblade to be the focal point of the design. The word Bourbon, proof, abv, and 750 ml will need to be horizontal. Creekhollow and Made in NC can be angled in the design.

Requirements
Must have
• Front Label will need to contain the followingBrand Name = SawmillsBourbon750 ml100 Proof50% ABVAged 3 years

```html
<!DOCTYPE html>
<html lang="en">
<head>
<meta charset="utf-8">
<title>Creekhollow Bourbon Label</title>
<link rel="stylesheet" href="https://fonts.googleapis.com/css2?family=Rye&family=Old+Standard+TT:wght@400;700&display=swap">
<style>
  :root {
    --canvas: #ffffff;
    --label-black: #000000;
    --gold-light: #fde58a;
    --gold: #e4b21c;
    --gold-deep: #b8860b;
    --forest-dark: #17130c;
    --forest-mid: #4a3f2a;
    --forest-light: #7d6c4c;
    --steel-light: #f4f6f8;
    --steel: #c8ccd2;
    --steel-dark: #9aa0a8;
    --vista-gold: #c9a66a;
    --vista-pale: #efe8da;
    --ink: #111111;
    --white: #ffffff;
  }
  * { margin: 0; padding: 0; box-sizing: border-box; }
  html, body {
    width: 1200px; height: 1200px; overflow: hidden;
    background: var(--canvas);
  }
  .canvas { position: relative; width: 1200px; height: 1200px; }
  .label {
    position: absolute; left: 141px; top: 44px; width: 926px; height: 1112px;
    background: var(--label-black);
  }
  .gold-frame {
    position: absolute; left: 54px; top: 50px; width: 818px; height: 1012px;
    padding: 9px;
    background: linear-gradient(90deg, var(--gold-deep), var(--gold-light) 50%, var(--gold-deep));
  }
  .forest-scene {
    position: relative; width: 100%; height: 100%; overflow: hidden;
    background:
      radial-gradient(ellipse at 50% 40%, rgba(0,0,0,0.55), transparent 70%),
      repeating-linear-gradient(90deg, var(--forest-dark) 0 22px, var(--forest-mid) 22px 30px, var(--forest-dark) 30px 58px, var(--forest-light) 58px 62px),
      var(--forest-dark);
  }
  .saw-blade {
    position: absolute; left: 113px; top: 313px; width: 584px; height: 584px;
  }
  .brand-name {
    position: absolute; left: 0; right: 0; top: 282px;
    text-align: center;
    font-family: "Rye", serif;
    font-size: 110px; line-height: 1;
    color: var(--gold);
    transform: rotate(-6deg);
  }
  .origin {
    position: absolute; left: 203px; top: 186px; width: 260px; height: 56px;
    text-align: center; white-space: nowrap;
    font-family: "Old Standard TT", serif; font-weight: 700;
    font-size: 46px; line-height: 56px; color: var(--white);
    transform: rotate(-15deg); transform-origin: center;
  }
  .product-type {
    position: absolute; left: 0; right: 0; top: 566px;
    text-align: center;
    font-family: "Old Standard TT", serif; font-weight: 700;
    font-size: 78px; line-height: 1; letter-spacing: 1px; color: var(--ink);
    -webkit-text-stroke: 1px var(--white);
  }
  .age-statement {
    position: absolute; left: 0; right: 0; top: 722px;
    text-align: center;
    font-family: "Old Standard TT", serif; font-weight: 700;
    font-size: 34px; line-height: 50px; color: var(--ink);
  }
  .age-statement .years { font-size: 50px; }
  .volume-band {
    position: absolute; left: 300px; top: 926px; width: 220px; height: 64px;
    border-radius: 32px; background: var(--label-black);
  }
  .spec {
    position: absolute;
    font-family: "Old Standard TT", serif; font-weight: 700;
    line-height: 1; color: var(--white); white-space: nowrap;
  }
  .spec.proof { left: 55px; top: 943px; font-size: 34px; }
  .spec.volume { left: 0; right: 0; top: 928px; text-align: center; font-size: 59px; }
  .spec.abv { right: 4px; top: 945px; font-size: 32px; }
</style>
</head>
<body>
<div class="canvas">
  <div class="label">
    <div class="gold-frame">
      <div class="forest-scene" role="img" aria-label="Dark sepia forest of tall Appalachian trees">
        <svg class="saw-blade" viewBox="0 0 584 584" role="img" aria-label="Silver circular sawblade framing a gold mountain panorama">
          <defs>
            <linearGradient id="steelFill" x1="0" y1="0" x2="1" y2="1">
              <stop offset="0" stop-color="#9aa0a8"/>
              <stop offset="0.45" stop-color="#f4f6f8"/>
              <stop offset="1" stop-color="#c8ccd2"/>
            </linearGradient>
            <linearGradient id="vistaFill" x1="0" y1="0" x2="0" y2="1">
              <stop offset="0" stop-color="#efe8da"/>
              <stop offset="0.45" stop-color="#c9a66a"/>
              <stop offset="1" stop-color="#efe8da"/>
            </linearGradient>
          </defs>
          <circle cx="292" cy="292" r="290" fill="url(#steelFill)"/>
          <circle cx="290" cy="288" r="224" fill="url(#vistaFill)" stroke="#111111" stroke-width="3"/>
        </svg>
        <div class="origin">Made in NC</div>
        <div class="brand-name">Creekhollow</div>
        <div class="product-type">BOURBON</div>
        <div class="age-statement">aged <span class="years">3</span> years</div>
        <div class="volume-band"></div>
        <div class="spec proof">100 proof</div>
        <div class="spec volume">750 ml</div>
        <div class="spec abv">50% abv</div>
      </div>
    </div>
  </div>
</div>
</body>
</html>
```